Flyer-Design für Veranstaltungen  von aufblasbaren Sport- und Funobjekten
Flyer-Design für Veranstaltungen von aufblasbaren Sport- und Funobjekten
Zielgruppe
Wir verleihen aufblasbare Sport- und Funobjekte zu Wasser und zu Land. Mit diesen Objekten führen wir auch Veranstaltungen durch und hierfür benötigen wir einen Flyer und ein 'prägendes' Bild mit Logo.
Aufgabenstellung
Der Flyer soll die nächsten Jahre verwendet werden. Das heisst, dass variable Angaben zu den Veranstaltungen notwendig sind wie z.B. Veranstaltungsort, Datum, Individuelle Bezeichnung. Die Veranstaltungen laufen generell unter dem Namen 'Wogtanz Hürden Duell', dann kann noch eine individuelle Bezeichnung dazu kommen wie 'Kiebinger Uferspieltage'. Individuell soll auch ein Hauptsponsor mit Logo angedruckt werden, z.B. 'sponsored by xxxxxx'.

```html
<!DOCTYPE html>
<html lang="de">
<head>
<meta charset="utf-8">
<title>Wogtanz Hürden Duell – Flyer</title>
<link href="https://fonts.googleapis.com/css2?family=Raleway:wght@300;400;600;700;800&display=swap" rel="stylesheet">
<style>
  :root{
    --page:#e4e4e4;
    --paper:#ffffff;
    --slate:#575f68;
    --slate-text:#55606b;
    --red:#e23c3c;
    --white:#ffffff;
    --grass-1:#6f9a4a;
    --grass-2:#4f7a38;
  }
  html,body{margin:0;padding:0;width:1200px;height:1200px;overflow:hidden;background:var(--page);}
  .flyer{position:absolute;left:204px;top:14px;width:792px;height:1172px;box-shadow:0 6px 18px rgba(0,0,0,.18);}
  .flyer text{font-family:"Raleway",sans-serif;}
  .tagline{fill:var(--white);font-weight:700;font-size:26px;}
  .headline{fill:var(--white);font-weight:800;font-size:50px;letter-spacing:.5px;}
  .subline{fill:var(--white);font-weight:400;font-size:31px;}
  .info-strong{fill:var(--white);font-weight:700;font-size:19px;}
  .info-light{fill:var(--white);font-weight:300;font-size:19px;}
  .brand{fill:var(--slate-text);font-weight:600;font-size:42px;}
  .powered{fill:var(--slate-text);font-weight:700;font-size:26px;}
  .sponsor-title{fill:var(--slate-text);font-weight:700;font-size:18px;}
  .sponsor-url{fill:var(--slate-text);font-weight:400;font-size:18px;}
</style>
</head>
<body>
<svg class="flyer" viewBox="0 0 788 1165" xmlns="http://www.w3.org/2000/svg">
  <defs>
    <linearGradient id="grass" x1="0" y1="0" x2="0" y2="1">
      <stop offset="0" stop-color="#7fa656"/>
      <stop offset=".5" stop-color="#c9d4cf"/>
      <stop offset="1" stop-color="#4f7a38"/>
    </linearGradient>
    <linearGradient id="pool" x1="0" y1="0" x2="0" y2="1">
      <stop offset="0" stop-color="#6f8e5a"/>
      <stop offset="1" stop-color="#3f8fb8"/>
    </linearGradient>
    <linearGradient id="course" x1="0" y1="0" x2="0" y2="1">
      <stop offset="0" stop-color="#7f9a62"/>
      <stop offset="1" stop-color="#c84a2a"/>
    </linearGradient>
    <linearGradient id="lake" x1="0" y1="0" x2="0" y2="1">
      <stop offset="0" stop-color="#5f8a4a"/>
      <stop offset="1" stop-color="#4f8f8a"/>
    </linearGradient>
  </defs>

  <rect class="paper" width="788" height="1165" fill="var(--paper)"/>

  <!-- lower info area -->
  <path class="info-band" d="M0 660 H788 V1080 L700 1074 L560 1080 L280 1074 L60 1082 L0 1078 Z" fill="var(--slate)"/>

  <!-- hero photo -->
  <path class="hero-photo" role="img" aria-label="Foto: zwei Personen in transparenten Bubble-Bällen auf einer Wiese"
        d="M0 140 L40 128 L200 118 L420 110 L560 114 L700 96 L750 120 L780 200 L770 260 L788 300 L780 420 L788 520 L0 560 Z"
        fill="url(#grass)"/>

  <!-- top slogan brush -->
  <path class="slogan-band" d="M360 0 H788 V120 L700 112 L560 118 L420 108 L330 114 L340 96 L300 88 L330 70 L290 60 L340 44 L310 30 L350 18 Z" fill="var(--slate)"/>
  <text class="tagline" x="565" y="46" text-anchor="middle">SPORT VERBINDET!</text>
  <text class="tagline" x="565" y="80" text-anchor="middle">SPORT MACHT SPASS!</text>

  <!-- brand mark -->
  <rect x="16" y="10" width="270" height="110" fill="var(--paper)"/>
  <circle cx="62" cy="66" r="20" fill="var(--red)"/>
  <text class="brand" x="96" y="80">wogtanz</text>

  <!-- red title brush -->
  <path class="title-band" d="M84 520 L300 506 L788 500 V670 L600 664 L400 672 L200 664 L52 670 L70 650 L40 636 L80 618 L56 600 L90 580 L66 560 L96 540 Z" fill="var(--red)"/>
  <text class="headline" x="148" y="577">HÜRDEN DUELL</text>
  <text class="subline" x="148" y="620">KIEBINGER UFERSPIELTAGE</text>

  <!-- event photos -->
  <path role="img" aria-label="Foto: aufblasbare Hindernisse im Schwimmbecken" d="M0 680 L265 654 L262 860 L0 880 Z" fill="url(#pool)" stroke="var(--white)" stroke-width="5"/>
  <path role="img" aria-label="Foto: roter aufblasbarer Hindernisparcours auf Rasen" d="M272 672 L525 690 L540 896 L250 880 Z" fill="url(#course)" stroke="var(--white)" stroke-width="5"/>
  <path role="img" aria-label="Foto: schwimmender Wasserparcours auf einem See" d="M518 684 L788 662 V860 L548 886 Z" fill="url(#lake)" stroke="var(--white)" stroke-width="5"/>

  <!-- icons -->
  <g class="icon-date" transform="translate(122 870)">
    <circle r="34" fill="var(--red)"/>
    <rect x="-15" y="-13" width="30" height="28" rx="3" fill="none" stroke="var(--white)" stroke-width="3"/>
    <line x1="-15" y1="-5" x2="15" y2="-5" stroke="var(--white)" stroke-width="3"/>
    <line x1="-8" y1="-18" x2="-8" y2="-10" stroke="var(--white)" stroke-width="3"/>
    <line x1="8" y1="-18" x2="8" y2="-10" stroke="var(--white)" stroke-width="3"/>
    <rect x="-3" y="1" width="9" height="8" fill="var(--white)"/>
  </g>
  <g class="icon-place" transform="translate(393 870)">
    <circle r="34" fill="var(--red)"/>
    <path d="M0 14 C-12 0 -13 -6 -13 -10 A13 13 0 0 1 13 -10 C13 -6 12 0 0 14 Z" fill="none" stroke="var(--white)" stroke-width="3"/>
    <circle cy="-10" r="4.5" fill="var(--white)"/>
    <ellipse cy="16" rx="17" ry="5" fill="none" stroke="var(--white)" stroke-width="3"/>
  </g>
  <g class="icon-time" transform="translate(668 870)">
    <circle r="34" fill="var(--red)"/>
    <circle cy="2" r="15" fill="none" stroke="var(--white)" stroke-width="3"/>
    <path d="M0 -5 V3 H7" fill="none" stroke="var(--white)" stroke-width="3"/>
    <path d="M-17 -10 A7 7 0 0 1 -9 -17 M17 -10 A7 7 0 0 0 9 -17" fill="none" stroke="var(--white)" stroke-width="3"/>
  </g>

  <!-- info columns -->
  <line x1="250" y1="912" x2="250" y2="1000" stroke="var(--white)" stroke-width="1.5" opacity=".7"/>
  <line x1="540" y1="912" x2="540" y2="1000" stroke="var(--white)" stroke-width="1.5" opacity=".7"/>

  <text class="info-strong" x="122" y="941" text-anchor="middle">04.07.2019</text>
  <text class="info-light" x="122" y="966" text-anchor="middle">BIS</text>
  <text class="info-strong" x="122" y="991" text-anchor="middle">07.07.2019</text>

  <text class="info-strong" x="393" y="941" text-anchor="middle">KIEBINGEN</text>
  <text class="info-light" x="393" y="966" text-anchor="middle">AM SPORTPLATZ</text>
  <text class="info-light" x="393" y="991" text-anchor="middle">GELÄNDE</text>

  <text class="info-strong" x="672" y="941" text-anchor="middle">TÄGLICH</text>
  <text class="info-light" x="672" y="966" text-anchor="middle">EINLASS: 8:00 UHR</text>
  <text class="info-light" x="672" y="991" text-anchor="middle">ENDE: 24 UHR</text>

  <!-- footer -->
  <text class="powered" x="45" y="1115">POWERED BY:</text>
  <rect x="276" y="1026" width="240" height="110" fill="var(--paper)"/>
  <circle cx="316" cy="1083" r="18" fill="var(--red)"/>
  <text class="brand" x="346" y="1096" style="font-size:38px">wogtanz</text>
  <text class="sponsor-title" x="561" y="1098">SPONSOREN INFO</text>
  <text class="sponsor-url" x="561" y="1123">WWW.WEBSITE.DE</text>
</svg>
</body>
</html>
```